Medical Services company. Need a website that blows the competition out of the water

We need a web site designed to draw attention to our many services offered. We are a Medical Services business based out of Pennsylvania. We provide basic first aid staffing for events and businesses such as but not limited to: Fairs, Festivals, Carnivals, Sporting events, Large gatherings where a first aid station is needed, Concerts, Businesses with first aid needs . We provide training and certifications that are tailored to the customers needs. We provide Covid-19 pre screening and temperature monitoring. Our professionals consist of individuals with Basic First Aid, Certified Nursing Assistants, Medical Assistants, Emergency Medical Responders (EMR), Emergency Medical Technicians (EMT), and Nurses. I do not know how many pages I will need since we offer multiple different services. Our main services provided are: First Aid services, Covid-19 pre screen and temperatures, and Training/Certifications. You will have to use stock photos for now until I can get some actual photographs of our team.I have uploaded a copy of my brochure so you can get some information from there as well.

Target Market(s)

-For the first Aid and Covid-19 services: All Businesses, Sporting events, Event organizers
-Training: Everyone.

Font styles to use
Sans Serif

Requirements
Must have
• My colors are what is in the logos and Gray , need to have a way for customers to request a quote, design that grabs their attention. Should have pictures of medical providers attending to the sick or injured. Both in a office setting and in an emergency out in public. Should have pictures of an ambulance. Should also have pictures of staff taking temperatures and asking pre screening questions.
Nice to have
• I'll get back to you on that one

```html
<!DOCTYPE html>
<html lang="en">
<head>
<meta charset="utf-8">
<title>Crestline Medical Services</title>
<link href="https://fonts.googleapis.com/css2?family=Poppins:wght@300;400;500;600;700;800&family=Lora:wght@500;600&display=swap" rel="stylesheet">
<style>
:root{
  --teal:#12b39a;
  --blue:#2323a8;
  --navy:#1a1a7e;
  --ink:#151515;
  --grey:#8a8a8a;
  --light:#f7f7f7;
  --white:#ffffff;
  --black:#000000;
}
*{margin:0;padding:0;box-sizing:border-box}
html,body{width:1200px;height:4501px;overflow:hidden}
body{font-family:'Poppins',sans-serif;color:var(--ink);background:var(--white);position:relative}
.abs{position:absolute}
.section-title{position:absolute;left:0;width:1200px;text-align:center;font-family:'Lora',serif;font-weight:500;font-size:31px;color:var(--ink)}
.divider{position:absolute;left:540px;width:120px;height:1px;background:#d6d6d6}
.divider::after{content:"";position:absolute;left:55px;top:-4px;width:9px;height:9px;border-radius:50%;background:#c9c9c9}
.divider.on-teal{background:rgba(255,255,255,.5)}
.divider.on-teal::after{background:var(--white)}
.lead{position:absolute;left:0;width:1200px;text-align:center;font-size:11px;line-height:19px;color:var(--grey)}
.btn{position:absolute;display:flex;align-items:center;justify-content:center;font-size:12px;font-weight:500;letter-spacing:.3px;box-shadow:3px 3px 0 rgba(0,0,0,.18)}
.btn-teal{background:var(--teal);color:var(--white)}
.btn-white{background:var(--white);color:var(--ink)}
.photo{position:absolute;border-radius:50%}

/* header */
.brand{left:60px;top:22px;display:flex;align-items:center;gap:10px}
.brand-mark{width:34px;height:34px;border-radius:50%;background:var(--blue)}
.brand-name{font-size:22px;font-weight:700;color:var(--blue);line-height:1}
.contact{display:flex;align-items:center;gap:14px;top:24px}
.contact-icon{width:40px;height:40px;border-radius:50%;background:var(--blue);display:flex;align-items:center;justify-content:center}
.contact-label{font-size:11px;color:var(--blue);font-weight:500}
.contact-value{font-size:12px;color:var(--ink);margin-top:5px}
.nav{left:60px;top:91px;width:1080px;height:51px;background:var(--teal);display:flex;align-items:center;z-index:5}
.nav a{color:var(--white);font-size:11px;text-decoration:none;text-transform:uppercase;height:51px;display:flex;align-items:center;padding:0 30px}
.nav a.active{background:var(--blue);padding:0 26px}
.search{position:absolute;left:660px;top:14px;width:390px;height:24px;border:1px solid rgba(255,255,255,.6);font-size:9px;color:var(--white);padding:6px 8px}

/* hero */
.hero{left:0;top:115px;width:1200px;height:650px;overflow:hidden;background:linear-gradient(90deg,#4a4a4a,#7b7b78 50%,#5f5f5f)}
.hero-title{left:61px;top:238px;font-size:44px;font-weight:800;line-height:52px;color:var(--teal);text-transform:uppercase;letter-spacing:1px;z-index:3}
.hero-sub{left:61px;top:353px;font-size:23px;line-height:34px;color:var(--white);font-weight:500;z-index:3}

/* welcome */
.welcome{left:0;top:765px;width:1200px;height:411px;background:var(--teal)}

/* specialize */
.col-title{position:absolute;width:400px;text-align:center;font-size:20px;font-weight:500;color:var(--blue)}
.col-text{position:absolute;width:370px;text-align:center;font-size:10.5px;line-height:19px;color:var(--grey)}

/* choose */
.choose{left:0;top:1918px;width:1200px;height:572px;background:var(--light)}
.venue{position:absolute;width:250px;height:250px;border-radius:50%;overflow:hidden;border:5px solid var(--white)}
.venue-label{position:absolute;left:0;bottom:0;width:100%;height:64px;background:rgba(35,35,168,.85);color:var(--white);font-size:13px;font-weight:500;text-align:center;line-height:18px;padding-top:8px}
.arrow{position:absolute;width:38px;height:38px;border-radius:50%;display:flex;align-items:center;justify-content:center}

/* services */
.service{position:absolute;left:599px;width:480px;display:flex;gap:24px}
.service-icon{width:60px;height:60px;border-radius:50%;flex:none;display:flex;align-items:center;justify-content:center}
.service h4{font-size:14px;font-weight:500;color:var(--ink);margin-top:-2px}
.service p{font-size:11px;line-height:19px;color:var(--grey);margin-top:6px}
.swatch{position:absolute;top:3085px;width:31px;height:31px}

/* help */
.help-bg{left:0;top:3608px;width:1200px;height:893px;background:var(--black)}
.help-title{left:136px;top:3690px;font-family:'Lora',serif;font-weight:500;font-size:30px;line-height:36px;color:var(--white)}
.help-text{left:136px;top:3772px;width:420px;font-size:11px;line-height:22px;color:var(--white)}
.help-call{left:136px;top:3870px;font-size:20px;font-weight:600;color:var(--white)}

/* footer */
.foot-head{position:absolute;top:4182px;font-family:'Lora',serif;font-size:15px;color:var(--teal)}
.foot-list{position:absolute;top:4226px;list-style:none;font-size:11px;color:var(--white)}
.foot-list li{height:30px}
.copyright{left:0;top:4470px;width:1200px;text-align:center;font-size:9px;color:#777}
</style>
</head>
<body>

<!-- HERO -->
<div class="abs hero" role="img" aria-label="Clinic waiting room photo background">
  <div class="photo" style="left:568px;top:-105px;width:840px;height:840px;background:radial-gradient(circle at 45% 40%,#b08a72,#6f7a80 55%,#4c5357)" role="img" aria-label="Health worker taking a masked woman's temperature with a thermometer"></div>
  <svg class="abs" style="left:0;top:485px" width="1200" height="165" viewBox="0 0 1200 165">
    <path d="M0 60 C180 0 420 40 600 80 C820 130 1000 110 1200 90 L1200 165 L0 165Z" fill="var(--navy)"/>
    <path d="M0 120 C200 40 420 70 620 100 C830 130 1020 120 1200 95 L1200 165 L0 165Z" fill="var(--teal)"/>
  </svg>
</div>
<div class="photo" style="left:330px;top:510px;width:238px;height:238px;border:6px solid #cfeee7;background:linear-gradient(135deg,#d7c3b2,#8fa3a8);z-index:2" role="img" aria-label="Two nurses reviewing a tablet together"></div>

<div class="abs hero-title">Crestline Medical<br>Services</div>
<div class="abs hero-sub">Providing All Of your Health<br>And Safety Needs</div>
<div class="btn btn-teal" style="left:61px;top:447px;width:119px;height:44px;box-shadow:none;z-index:3">LEARN MORE</div>

<!-- HEADER -->
<div class="abs brand"><span class="brand-mark"></span><span class="brand-name">Crestline</span></div>

<div class="abs contact" style="left:480px">
  <div class="contact-icon"><svg width="18" height="18" viewBox="0 0 24 24"><path fill="#fff" d="M6.6 10.8a15 15 0 006.6 6.6l2.2-2.2c.3-.3.7-.4 1-.2 1.1.4 2.3.6 3.6.6.6 0 1 .4 1 1V20c0 .6-.4 1-1 1A17 17 0 013 4c0-.6.4-1 1-1h3.5c.6 0 1 .4 1 1 0 1.3.2 2.5.6 3.6.1.3 0 .7-.2 1z"/></svg></div>
  <div><div class="contact-label">Call Us On</div><div class="contact-value">717-555-0142</div></div>
</div>
<div class="abs contact" style="left:660px">
  <div class="contact-icon"><svg width="18" height="18" viewBox="0 0 24 24"><rect x="3" y="6" width="18" height="12" fill="none" stroke="#fff" stroke-width="2"/><path d="M3 6l9 7 9-7" fill="none" stroke="#fff" stroke-width="2"/></svg></div>
  <div><div class="contact-label">Email Us</div><div class="contact-value">care@crestlinemed.com</div></div>
</div>
<div class="abs contact" style="left:922px">
  <div class="contact-icon"><svg width="18" height="18" viewBox="0 0 24 24" fill="none" stroke="#fff" stroke-width="1.8"><circle cx="12" cy="12" r="9"/><ellipse cx="12" cy="12" rx="4" ry="9"/><path d="M3 12h18"/></svg></div>
  <div><div class="contact-label">Globe</div><div class="contact-value">www.crestlinemed.com</div></div>
</div>

<nav class="abs nav">
  <a class="active">Home</a><a>About</a><a>Services</a><a>Request a Quote</a><a>Contact Us</a>
  <div class="search">Search Here.....
    <svg class="abs" style="right:6px;top:5px" width="12" height="12" viewBox="0 0 24 24" fill="none" stroke="#fff" stroke-width="2.5"><circle cx="10" cy="10" r="7"/><path d="M15 15l6 6"/></svg>
  </div>
</nav>

<!-- WELCOME -->
<div class="abs welcome"></div>
<div class="section-title" style="top:822px;color:var(--white)">Welcome To Crestline Medical Services</div>
<div class="divider on-teal" style="top:882px"></div>
<div class="lead" style="top:911px;color:var(--white)">Lorem ipsum dolor sit amet, consectetur adipiscing elit, sed do eiusmod tempor incididunt ut labore et dolore<br>magna aliqua. Ut enim ad minim veniam, quis nostrud exercitation ullamco laboris nisi ut aliquip ex ea commodo<br>consequat. Duis aute irure dolor cillum dolore eu fugiat nulla pariatur.</div>
<div class="lead" style="top:986px;color:var(--white)">Lorem ipsum dolor sit amet, consectetur adipiscing elit, sed do eiusmod tempor incididunt ut labore et dolore<br>consequat. Duis aute irure dolor cillum dolore eu fugiat nulla pariatur.</div>
<div class="btn btn-white" style="left:538px;top:1051px;width:121px;height:44px">ABOUT US</div>

<!-- SPECIALIZE -->
<div class="section-title" style="top:1250px">We Specialize in two things.</div>
<div class="divider" style="top:1308px"></div>
<div class="abs" style="left:600px;top:1350px;width:1px;height:490px;background:#e2e2e2"></div>

<div class="col-title" style="left:122px;top:1346px">Keeping You Safe</div>
<div class="photo" style="left:235px;top:1415px;width:245px;height:245px;background:linear-gradient(135deg,#e6ddd6,#9aa5b3)" role="img" aria-label="Doctor examining a patient with a stethoscope"></div>
<div class="photo" style="left:170px;top:1415px;width:125px;height:125px;border:4px solid #fff;background:linear-gradient(135deg,#c9d3dc,#4d7fa8)" role="img" aria-label="Smiling nurse in blue scrubs"></div>
<div class="col-text" style="left:137px;top:1690px">you will notice the difference when you choose Crestline for your business or event. By having trained, Professional, Responders present, your staff will feel safer and morale will improve, productivity will increase and incidents will reduce.</div>
<div class="btn btn-teal" style="left:261px;top:1793px;width:120px;height:44px">LEARN MORE</div>

<div class="col-title" style="left:677px;top:1346px">Training Services</div>
<div class="photo" style="left:720px;top:1415px;width:240px;height:240px;background:linear-gradient(135deg,#a9adb0,#5e6468)" role="img" aria-label="Man practising with an oxygen mask during training"></div>
<div class="photo" style="left:905px;top:1412px;width:125px;height:125px;border:4px solid #fff;background:linear-gradient(135deg,#e9e2dc,#a27963)" role="img" aria-label="Smiling instructor in a white coat"></div>
<div class="col-text" style="left:692px;top:1690px">At Crestline we have a broad range of health and Safety classes to suit your every need. We take pride in our instructors who have years of experience instructing quality built classes. We make learning CPR fun and affordable for the everyday public and healthcare providers.</div>
<div class="btn btn-teal" style="left:816px;top:1793px;width:120px;height:44px">LEARN MORE</div>

<!-- CHOOSE US -->
<div class="abs choose"></div>
<div class="section-title" style="top:1977px">We Choose Us</div>
<div class="divider" style="top:2036px"></div>
<div class="lead" style="top:2066px">We provide basic first aid and covid-19 pre screening and temperature<br>monitoring for, but not limited to:</div>

<div class="venue" style="left:144px;top:2155px;background:linear-gradient(135deg,#6f7d95,#2e3d5c)" role="img" aria-label="Warehouse with tall storage racks"><div class="venue-label">Industrial<br>Buildings</div></div>
<div class="venue" style="left:363px;top:2155px;background:linear-gradient(135deg,#c9c6c0,#6b5f55)" role="img" aria-label="Speaker addressing a seated audience"><div class="venue-label">Large<br>Gatherings</div></div>
<div class="venue" style="left:584px;top:2155px;background:linear-gradient(135deg,#e4ecf3,#8fa6bd)" role="img" aria-label="Clean manufacturing floor with machinery"><div class="venue-label">Manufacturing<br>Facilities</div></div>
<div class="venue" style="left:804px;top:2155px;background:linear-gradient(135deg,#efe6d6,#8c7a63)" role="img" aria-label="Guests toasting at a celebration"><div class="venue-label">Special<br>Events</div></div>

<div class="arrow" style="left:41px;top:2261px;background:var(--teal)"><svg width="12" height="12" viewBox="0 0 12 12"><path d="M8 2L4 6l4 4" fill="none" stroke="#fff" stroke-width="1.6"/></svg></div>
<div class="arrow" style="left:1121px;top:2261px;border:1.5px solid var(--teal);background:var(--white)"><svg width="12" height="12" viewBox="0 0 12 12"><path d="M4 2l4 4-4 4" fill="none" stroke="var(--teal)" stroke-width="1.6"/></svg></div>

<!-- SERVICES -->
<div class="section-title" style="top:2555px">Our Services</div>
<div class="divider" style="top:2614px"></div>
<div class="lead" style="top:2643px">Lorem ipsum dolor sit amet, consectetur adipiscing elit, sed do eiusmod<br>tempor incididunt ut labore et dolore magna aliqua.</div>
<div class="abs" style="left:135px;top:2715px;width:390px;height:337px;border-radius:6px;background:linear-gradient(135deg,#9a9fa6,#3f4f7a 60%,#2d3553)" role="img" aria-label="Responders performing CPR with a defibrillator on a patient"></div>

<div class="service" style="top:2712px">
  <div class="service-icon" style="background:var(--blue)"><svg width="26" height="26" viewBox="0 0 24 24" fill="none" stroke="#fff" stroke-width="1.6"><rect x="3" y="7" width="18" height="13" rx="1"/><path d="M9 7V4h6v3M12 10v7M8.5 13.5h7"/></svg></div>
  <div><h4>First Aid</h4><p>For patient with minor to life threatening<br>injuries or illness</p></div>
</div>
<div class="service" style="top:2804px">
  <div class="service-icon" style="background:var(--teal)"><svg width="28" height="28" viewBox="0 0 24 24" fill="none" stroke="#fff" stroke-width="1.5"><rect x="2" y="7" width="13" height="9"/><path d="M15 10h4l3 3v3h-7M7 10v4M5 12h4"/><circle cx="6" cy="18" r="1.6"/><circle cx="18" cy="18" r="1.6"/></svg></div>
  <div><h4>Onsite Care</h4><p>Provide immediate care by removing the delay in response,<br>assessment and treatment</p></div>
</div>
<div class="service" style="top:2896px">
  <div class="service-icon" style="background:var(--teal)"><svg width="26" height="26" viewBox="0 0 24 24" fill="none" stroke="#fff" stroke-width="1.6"><path d="M12 20s-7-4.5-7-10a4 4 0 017-2.6A4 4 0 0119 10c0 5.5-7 10-7 10z"/><path d="M6 12h3l2-3 2 5 2-2h3"/></svg></div>
  <div><h4>Trauma/Resuscitaion</h4><p>Provide immediate and LIFESAVING treatment for patients with life<br>Threatening injuries or illness</p></div>
</div>
<div class="service" style="top:2988px">
  <div class="service-icon" style="background:var(--teal)"><svg width="26" height="26" viewBox="0 0 24 24" fill="none" stroke="#fff" stroke-width="1.6"><path d="M12 3l7 3v5c0 5-3.5 8-7 10-3.5-2-7-5-7-10V6z"/><path d="M9 12l2 2 4-4"/></svg></div>
  <div><h4>Covid-19 Pre Screening</h4><p>Pre Screening and Temprature Monitoring of individuals entering<br>your facility or event</p></div>
</div>
<div class="swatch" style="left:867px;background:var(--black)"></div>
<div class="swatch" style="left:904px;background:var(--blue)"></div>
<div class="swatch" style="left:941px;background:var(--teal)"></div>

<!-- FEEDBACK -->
<div class="abs" style="left:0;top:3127px;width:1200px;height:481px;background:#fbfbfb"></div>
<div class="section-title" style="top:3200px">Client's Feedback</div>
<div class="divider" style="top:3258px"></div>
<div class="abs" style="left:531px;top:3315px;width:64px;height:64px;border-radius:50%;background:var(--teal);display:flex;align-items:center;justify-content:center;color:#fff;font-family:'Lora',serif;font-size:46px;line-height:1;padding-top:18px">&ldquo;</div>
<div class="photo" style="left:587px;top:3303px;width:80px;height:80px;border:3px solid var(--blue);background:linear-gradient(135deg,#d8dde3,#53606f)" role="img" aria-label="Client portrait"></div>
<div class="arrow" style="left:210px;top:3418px;border:1.5px solid var(--teal)"><svg width="12" height="12" viewBox="0 0 12 12"><path d="M8 2L4 6l4 4" fill="none" stroke="var(--teal)" stroke-width="1.6"/></svg></div>
<div class="arrow" style="left:948px;top:3418px;background:#cdeee8"><svg width="12" height="12" viewBox="0 0 12 12"><path d="M4 2l4 4-4 4" fill="none" stroke="var(--teal)" stroke-width="1.6"/></svg></div>
<div class="lead" style="top:3412px">Lorem ipsum dolor sit amet, consectetur adipiscing elit, sed do eiusmod tempor incididunt ut labore et dolore<br>magna aliqua. Ut enim ad minim veniam, quis nostrud exercitation ullamco laboris nisi ut aliquip ex ea<br>commodo consequat. Duis aute irure dolor in reprehenderit in voluptate velit esse.</div>
<div class="abs" style="left:0;top:3500px;width:1200px;text-align:center;font-size:13px;color:var(--blue);font-weight:500">- Client's Name</div>

<!-- HELP -->
<div class="abs help-bg"></div>
<svg class="abs" style="left:0;top:3608px" width="1200" height="560" viewBox="0 0 1200 560">
  <path d="M0 0H1200V500 C1000 560 820 470 600 430 C380 390 180 440 0 460Z" fill="var(--blue)"/>
  <path d="M0 0H1200V470 C1000 530 820 450 600 410 C380 370 180 420 0 440Z" fill="var(--teal)"/>
</svg>
<div class="photo" style="left:650px;top:3682px;width:370px;height:370px;background:linear-gradient(135deg,#d9d2c8,#9a8f84 50%,#c9c3bb)" role="img" aria-label="Ambulance parked in front of a hospital building"></div>
<div class="photo" style="left:136px;top:3938px;width:172px;height:172px;border:5px solid #8a8a8a;background:linear-gradient(135deg,#e7e0d8,#5e8fa8)" role="img" aria-label="Paramedic in high-visibility vest assisting a patient"></div>
<div class="abs help-title">Crestline Medical Services Here<br>to help</div>
<div class="abs help-text">Lorem ipsum dolor sit amet, consectetur adipiscing elit, sed do eiusmod tempor incididunt ut labore et dolore magna aliqua. Ut enim ad minim veniam, quis nostrud exercitation ullamco laboris nisi ut aliquip ex ea cillum dolore eu fugiat nulla pariatur.</div>
<div class="abs help-call">Call Us On&nbsp; : &nbsp;717-555-0142</div>

<!-- FOOTER -->
<div class="abs" style="left:130px;top:4215px;display:flex;align-items:center;gap:8px">
  <span style="width:22px;height:22px;border-radius:50%;background:var(--teal)"></span>
  <span style="font-size:18px;font-weight:700;color:var(--white)">Crestline</span>
</div>
<div class="btn btn-teal" style="left:128px;top:4331px;width:120px;height:42px;box-shadow:3px 3px 0 rgba(255,255,255,.25)">GET A QUOTE</div>

<div class="foot-head" style="left:337px">Services</div>
<ul class="foot-list" style="left:337px"><li>First Aid</li><li>Onsite Care</li><li>Trauma/Resuscitaion</li><li>Covid-19 Pre Screening</li></ul>
<div class="foot-head" style="left:613px">Links</div>
<ul class="foot-list" style="left:613px"><li>Home</li><li>About</li><li>Services</li><li>Request a Quote</li><li>Contact Us</li></ul>
<div class="foot-head" style="left:889px">Get In Touch</div>
<ul class="foot-list" style="left:889px"><li>Call Us&nbsp; : &nbsp;717-555-0142</li><li>Email Us&nbsp;&nbsp; : &nbsp;care@crestlinemed.com</li><li>Globe&nbsp; : &nbsp;www.crestlinemed.com</li></ul>

<div class="abs" style="left:60px;top:4455px;width:1080px;height:1px;background:#2a2a2a"></div>
<div class="abs copyright">Copyright © CRESTLINE MEDICAL SERVICES - 2020. All Right Reserved.</div>

</body>
</html>
```